Website Design for Ridgeline Forgecraft And Decorative Steel LLC

Ridgeline Forgecraft & Decorative Steel is a veteran-owned and operated metal fabrication firm with decades of combined experience. We deliver custom, ornamental, and architectural metal solutions designed to meet the demands of commercial construction projects.

Our team specializes in fabricating and installing metal stairs, guardrails, handrails, railings, fencing, and ornamental metals that combined durability, code compliance, and visual appeal. We are a Small Business Enterprise (SBE), Veteran Business Enterprise (VBE), Service-Disabled Veteran-Owned Small Business (SDVOSB), and Veteran Friendly Business Enterprise (VFBE) Certified firm.

We are looking for a designer to create our website so that it can be used at our domain www.ridgelineforgecraftllc.example that we have sourced through Netplotter.example

We also have already created our corporate logo through crowdsource that can be incorporated into the web design.

Target Market(s)

General Contractors, Construction Managers, and Architects

Industry/Entity Type

Construction

Coding

Coded - Design and coding required

Number of Pages Required

5+ page

Requirements
Must have
• Company logo (Zip File Uploaded), About Us, Product Solutions, Target Market (See uploaded flyer)
Nice to have
• Patriotic Theme (American)
Should not have
• Web store

```html
<!DOCTYPE html>
<html lang="en">
<head>
<meta charset="utf-8">
<title>Ridgeline Forgecraft &amp; Decorative Steel</title>
<link href="https://fonts.googleapis.com/css2?family=Rammetto+One&family=Roboto:wght@400;500;700;900&family=Poppins:wght@400;500;600&display=swap" rel="stylesheet">
<style>
:root{
  --navy:#0b2a6e;
  --navy-deep:#082057;
  --red:#c0123a;
  --pink:#f3c6cf;
  --ink:#1b1b1f;
  --grey:#e9e9ec;
  --badge:#dfe3ec;
  --footer:#1c1d22;
}
*{margin:0;padding:0;box-sizing:border-box}
html,body{width:1200px;height:3971px;overflow:hidden;background:#fff}
body{font-family:"Poppins",sans-serif;color:var(--ink);position:relative}
.abs{position:absolute}
.btn{position:absolute;display:flex;align-items:center;justify-content:center;font-family:"Roboto",sans-serif;font-weight:700;font-size:11px;letter-spacing:.3px;color:#fff;background:var(--navy);text-transform:uppercase}
.btn.dark{background:#0c0c0e}
.heading{font-family:"Roboto",sans-serif;font-weight:900;color:var(--red);font-size:29px;letter-spacing:-.3px}
.rule{display:block;width:44px;height:2px;background:var(--red);margin-top:8px}
.rule.center{margin:8px auto 0}

/* header */
.site-header{position:absolute;top:0;left:0;width:1200px;height:62px;background:#fff;z-index:2}
.nav{position:absolute;left:155px;top:24px;display:flex;gap:22px;font-family:"Roboto",sans-serif;font-weight:500;font-size:10.5px;color:var(--navy)}
.nav .active{color:var(--red);text-decoration:underline}
.phone{position:absolute;left:802px;top:24px;font-family:"Roboto",sans-serif;font-weight:500;font-size:12px;color:var(--ink);display:flex;align-items:center;gap:6px}
.brand{position:absolute;left:529px;top:-2px;width:142px;height:142px;border-radius:50%;background:#fff;border:3px solid var(--navy);display:flex;align-items:center;justify-content:center;text-align:center;z-index:3;font-family:"Roboto",sans-serif;font-weight:900;font-size:16px;line-height:1.1;color:var(--navy)}

/* hero */
.hero{position:absolute;top:62px;left:0;width:1200px;height:532px;background:radial-gradient(ellipse at 70% 40%,#c7651f 0%,#6a2c12 35%,#22120c 70%,#120b08 100%)}
.hero h1{position:absolute;top:194px;left:0;width:1200px;text-align:center;font-family:"Rammetto One",sans-serif;font-size:44px;line-height:1.02;color:#fff;font-weight:400}

/* about */
.about-photo{position:absolute;left:178px;top:684px;width:360px;height:360px;border-radius:50%;border:3px solid var(--red);padding:6px}
.about-photo div{width:100%;height:100%;border-radius:50%;background:linear-gradient(160deg,#8fa3b8,#5d6f83 55%,#3d4a59)}
.dot{position:absolute;border-radius:50%}
.about-text{position:absolute;left:612px;top:722px;width:428px}
.about-text p{font-size:10.2px;line-height:1.55;color:#333;margin-top:16px}
.about-text p b{font-weight:600;color:#111}

/* markets */
.markets{position:absolute;top:1141px;left:0;width:682px;height:487px;background:var(--navy)}
.markets-photo{position:absolute;top:1141px;left:682px;width:518px;height:487px;background:linear-gradient(150deg,#a9b8c9,#6c7f94 50%,#3b4a5d)}
.market{position:absolute;width:160px;text-align:center;font-family:"Roboto",sans-serif;font-weight:500;font-size:12px;line-height:1.3;color:#fff}
.icon-ring{width:88px;height:88px;border-radius:50%;background:#fff;border:4px solid #d7dced;margin:0 auto 8px;display:flex;align-items:center;justify-content:center}

/* products */
.card{position:absolute;width:204px;height:230px}
.card .shot{width:204px;height:188px;background:linear-gradient(160deg,#a7b0ba,#6e7780)}
.card .label{position:absolute;left:10px;top:171px;width:182px;height:56px;background:#fff;box-shadow:0 4px 12px rgba(0,0,0,.12);display:flex;flex-direction:column;justify-content:center;padding:0 16px;font-family:"Roboto",sans-serif;font-weight:500;font-size:12px;line-height:1.3;color:#111}
.card .label small{font-size:7.5px;font-weight:400;color:#444;line-height:1.2}

/* experience */
.experience{position:absolute;top:2383px;left:0;width:1200px;height:385px;background:linear-gradient(180deg,#232a38,#1a2130 60%,#141a26)}
.stat{position:absolute;width:200px;text-align:center;top:2536px;font-family:"Roboto",sans-serif;font-weight:700;font-size:12px;line-height:1.3;color:#fff}
.stat .icon-ring{width:90px;height:90px;border:4px solid #cfd6e8;margin-bottom:14px}

/* why */
.reason{position:absolute;display:flex;gap:11px;width:230px}
.reason .tick{flex:none;width:20px;height:20px;border-radius:50%;background:var(--red);display:flex;align-items:center;justify-content:center;margin-top:4px}
.reason h4{font-family:"Roboto",sans-serif;font-weight:700;font-size:12px;color:#111}
.reason p{font-size:9px;line-height:1.45;color:#333;margin-top:2px}
.why-photo{position:absolute;left:681px;top:2845px;width:360px;height:360px;border-radius:50%;border:3px solid var(--red);padding:5px}
.why-photo div{width:100%;height:100%;border-radius:50%;background:radial-gradient(circle at 45% 60%,#e8c27a 0%,#3a5d88 25%,#1c3150 60%,#0f1c30)}

/* form */
.contact{position:absolute;top:3320px;left:0;width:1200px;height:412px;background:linear-gradient(180deg,#14285a,#0d1f4a)}
.field{position:absolute;width:223px}
.field label{display:block;font-size:9.5px;color:#fff;margin-bottom:6px}
.field .input{height:30px;background:#fff;border:1px solid #cfd3dc;font-size:9px;color:#aab;padding:8px 12px}

/* footer */
.footer{position:absolute;top:3732px;left:0;width:763px;height:208px;background:var(--footer)}
.footer-badges{position:absolute;top:3732px;left:763px;width:437px;height:208px;background:var(--grey)}
.foot-col{position:absolute;top:3783px;font-size:10.5px;color:#fff;line-height:1.4}
.foot-col h5{font-family:"Roboto",sans-serif;font-weight:700;font-size:11.5px;color:var(--red);margin-bottom:12px}
.foot-col li{list-style:none;margin-bottom:8px;display:flex;gap:10px}
.bottom-bar{position:absolute;top:3940px;left:0;width:1200px;height:31px;background:var(--red);font-size:10.5px;color:#fff}
</style>
</head>
<body>

<header class="site-header">
  <nav class="nav"><span class="active">HOME</span><span>ABOUT US</span><span>PRODUCTS</span><span>CONTACT US</span></nav>
  <div class="phone">
    <svg width="11" height="11" viewBox="0 0 24 24"><path fill="#c0123a" d="M6.6 10.8a15 15 0 0 0 6.6 6.6l2.2-2.2a1 1 0 0 1 1-.25 11.4 11.4 0 0 0 3.6.6 1 1 0 0 1 1 1V20a1 1 0 0 1-1 1A17 17 0 0 1 3 4a1 1 0 0 1 1-1h3.5a1 1 0 0 1 1 1c0 1.25.2 2.45.6 3.6a1 1 0 0 1-.25 1z"/></svg>
    (555) 014-2280
  </div>
  <div class="btn" style="left:925px;top:15px;width:119px;height:33px">Quick Inquiry</div>
</header>
<div class="brand">Ridgeline<br>Forgecraft</div>

<section class="hero" role="img" aria-label="Welder in protective gear cutting steel with sparks flying in a workshop">
  <h1>Best Welding &amp;<br>Metal Works</h1>
  <div class="btn dark" style="left:480px;top:303px;width:112px;height:32px">Contact Now</div>
  <div class="btn dark" style="left:600px;top:303px;width:119px;height:32px">Our Products</div>
</section>

<!-- about -->
<div class="dot" style="left:131px;top:869px;width:56px;height:56px;background:var(--pink)"></div>
<div class="dot" style="left:265px;top:1025px;width:28px;height:28px;background:var(--pink)"></div>
<div class="dot" style="left:485px;top:707px;width:24px;height:24px;background:#c9cfdc"></div>
<div class="about-photo" role="img" aria-label="Two engineers in hard hats reviewing plans in a factory"><div></div></div>
<div class="dot" role="img" aria-label="Round national flag badge" style="left:438px;top:948px;width:80px;height:80px;border:3px solid #fff;background:var(--badge)"></div>
<div class="about-text">
  <h2 class="heading">About Us</h2><span class="rule" style="width:12px"></span>
  <p>Ridgeline Forgecraft &amp; Decorative Steel LLC Is A Veteran-Owned And Operated Metal Fabrication Firm With Decades Of Combined Experience. We Deliver <b>Custom, Ornamental, And Architectural Metal Solutions</b> Designed To Meet The Demands Of Commercial Construction Projects.</p>
  <p>Our Team Specializes In Fabricating And Installing Metal Stairs, Guardrails, Handrails, Railings, Fencing, And Ornamental Metals That Combine Durability, Code Compliance, And Visual Appeal. We Are A <b>Small Business Enterprise (SBE), Veteran Business Enterprise (VBE), Service-Disabled Veteran-Owned Small Business (SDVOSB), And Veteran Friendly Business Enterprise (VFBE)</b> Certified Firm.</p>
</div>
<div class="btn" style="left:612px;top:962px;width:101px;height:31px">Read More</div>

<!-- markets -->
<section class="markets">
  <h2 class="heading" style="position:absolute;left:0;width:746px;text-align:center;top:62px">Markets Served<span class="rule center" style="width:40px"></span></h2>
  <div class="market" style="left:122px;top:141px"><div class="icon-ring"><svg width="34" height="34" viewBox="0 0 34 34" fill="none" stroke="#0b2a6e" stroke-width="2"><rect x="6" y="8" width="22" height="22"/><path d="M11 14h4M19 14h4M11 20h4M19 20h4M15 30v-5h4v5"/></svg></div>Commercial<br>Construction</div>
  <div class="market" style="left:282px;top:141px"><div class="icon-ring"><svg width="34" height="34" viewBox="0 0 34 34" fill="none" stroke="#0b2a6e" stroke-width="2"><path d="M4 30V16l8 5v-5l8 5v-5l8 5v9z"/><path d="M24 18V6h4v14"/></svg></div>Industrial<br>Facilities</div>
  <div class="market" style="left:444px;top:141px"><div class="icon-ring"><svg width="34" height="34" viewBox="0 0 34 34" fill="none" stroke="#0b2a6e" stroke-width="2"><path d="M6 6h22M8 10h18M17 10v12M10 16c0 6 14 6 14 0M12 28h10"/></svg></div>Manufacturing<br>Plants</div>
  <div class="market" style="left:202px;top:282px"><div class="icon-ring"><svg width="34" height="34" viewBox="0 0 34 34" fill="none" stroke="#0b2a6e" stroke-width="2"><circle cx="17" cy="17" r="11"/><circle cx="17" cy="17" r="4" stroke="#2bb673"/></svg></div>Government &amp;<br>Defense Projects</div>
  <div class="market" style="left:375px;top:282px"><div class="icon-ring"><svg width="34" height="34" viewBox="0 0 34 34" fill="none" stroke="#0b2a6e" stroke-width="2"><path d="M6 16h22a11 11 0 0 1-22 0z"/><path d="M17 16V8" stroke="#2bb673"/></svg></div>Built Environment &amp;<br>Infrastructure</div>
</section>
<div class="markets-photo" role="img" aria-label="Female worker in a hard hat talking with an engineer in a steel warehouse"></div>

<!-- products -->
<h2 class="heading abs" style="top:1697px;left:0;width:1200px;text-align:center">Product Solutions<span class="rule center"></span></h2>
<div class="card" style="left:156px;top:1767px"><div class="shot" role="img" aria-label="Steel stair with yellow railing at a building entrance"></div><div class="label">Special Promotion<br>Giveaway</div></div>
<div class="card" style="left:384px;top:1767px"><div class="shot" role="img" aria-label="Catwalk with metal handrails"></div><div class="label">Catwalks &amp; Platforms</div></div>
<div class="card" style="left:612px;top:1767px"><div class="shot" role="img" aria-label="Custom fabricated mesh stair railing"></div><div class="label">Custom Metal<br>Fabrication</div></div>
<div class="card" style="left:840px;top:1767px"><div class="shot" role="img" aria-label="Outdoor galvanized steel staircase with railings"></div><div class="label">Decorative Metal<br>Railings</div></div>
<div class="card" style="left:156px;top:2017px"><div class="shot" role="img" aria-label="Terrace with glazed metal railing panels"></div><div class="label">Decorative Glazed<br>Railings</div></div>
<div class="card" style="left:384px;top:2017px"><div class="shot" role="img" aria-label="Interior pan stair with metal guardrails"></div><div class="label">Pan Stairs</div></div>
<div class="card" style="left:612px;top:2017px"><div class="shot" role="img" aria-label="Glass stair with pipe and tube railing"></div><div class="label">Pipe &amp; Tube Railings</div></div>
<div class="card" style="left:840px;top:2017px"><div class="shot" role="img" aria-label="Riverside walkway with black metal fence"></div><div class="label">Miscellaneous Metals<small>(Platforms, Ladders, Embeds, Custom Assemblies)</small></div></div>
<div class="btn" style="left:541px;top:2276px;width:118px;height:31px">Contact Now</div>

<!-- experience -->
<section class="experience" role="img" aria-label="Dim workshop with welders at work in the background">
  <h2 class="heading" style="position:absolute;top:80px;left:0;width:1200px;text-align:center">Experience Snapshot<span class="rule center"></span></h2>
</section>
<div class="stat" style="left:195px"><div class="icon-ring"><svg width="34" height="34" viewBox="0 0 34 34" fill="none" stroke="#0b2a6e" stroke-width="2"><rect x="8" y="14" width="18" height="14"/><path d="M12 14V8h10v6" stroke="#c0123a"/></svg></div>Decades Of Combined<br>Fabrication Experience</div>
<div class="stat" style="left:397px"><div class="icon-ring"><svg width="34" height="34" viewBox="0 0 34 34" fill="none" stroke="#0b2a6e" stroke-width="2"><path d="M6 6h22M8 10h18M17 10v12M10 16c0 6 14 6 14 0M12 28h10"/></svg></div>Proven Track Record<br>With Top-Tier National<br>Manufacturers</div>
<div class="stat" style="left:603px"><div class="icon-ring"><svg width="34" height="34" viewBox="0 0 34 34" fill="none" stroke="#0b2a6e" stroke-width="2"><path d="M4 30V16l8 5v-5l8 5v-5l8 5v9z"/></svg></div>Government, Commercial,<br>And Industrial Project<br>Execution Expertise</div>
<div class="stat" style="left:807px"><div class="icon-ring"><svg width="34" height="34" viewBox="0 0 34 34" fill="none" stroke="#0b2a6e" stroke-width="2"><circle cx="17" cy="17" r="11"/><circle cx="17" cy="17" r="5"/></svg></div>On-Time, Precision-<br>Built Projects<br>Nationwide</div>

<!-- why -->
<h2 class="heading abs" style="left:156px;top:2856px">Why Contractors Choose Us<span class="rule"></span></h2>
<div class="reason" style="left:156px;top:2934px"><span class="tick"><svg width="8" height="8" viewBox="0 0 8 8"><path d="M2.5 1l3 3-3 3" stroke="#fff" stroke-width="1.6" fill="none"/></svg></span><div><h4>Stay On Schedule</h4><p>We Deliver Projects On Time, Meeting<br>Even Aggressive Timelines</p></div></div>
<div class="reason" style="left:156px;top:2999px"><span class="tick"><svg width="8" height="8" viewBox="0 0 8 8"><path d="M2.5 1l3 3-3 3" stroke="#fff" stroke-width="1.6" fill="none"/></svg></span><div><h4>Get The Look You Want</h4><p>From Functional Handrails To Custom<br>Ornamental Features</p></div></div>
<div class="reason" style="left:156px;top:3064px"><span class="tick"><svg width="8" height="8" viewBox="0 0 8 8"><path d="M2.5 1l3 3-3 3" stroke="#fff" stroke-width="1.6" fill="none"/></svg></span><div><h4>Lower Costs Over Time</h4><p>Durable Materials Reduce Maintenance<br>And Extend Performance</p></div></div>
<div class="reason" style="left:156px;top:3127px"><span class="tick"><svg width="8" height="8" viewBox="0 0 8 8"><path d="M2.5 1l3 3-3 3" stroke="#fff" stroke-width="1.6" fill="none"/></svg></span><div><h4>American Made</h4><p>Fabricated With Pride In The USA,<br>Supporting Local Industries</p></div></div>
<div class="reason" style="left:399px;top:2934px;width:240px"><span class="tick"><svg width="8" height="8" viewBox="0 0 8 8"><path d="M2.5 1l3 3-3 3" stroke="#fff" stroke-width="1.6" fill="none"/></svg></span><div><h4>Modern Technology</h4><p>Leveraging Advanced Tools For<br>Precision, Efficiency, And Quality Results</p></div></div>
<div class="reason" style="left:399px;top:2999px;width:240px"><span class="tick"><svg width="8" height="8" viewBox="0 0 8 8"><path d="M2.5 1l3 3-3 3" stroke="#fff" stroke-width="1.6" fill="none"/></svg></span><div><h4>Value Engineering Options</h4><p>Practical Solutions To Balance Cost,<br>Performance, And Aesthetics</p></div></div>
<div class="reason" style="left:399px;top:3064px;width:240px"><span class="tick"><svg width="8" height="8" viewBox="0 0 8 8"><path d="M2.5 1l3 3-3 3" stroke="#fff" stroke-width="1.6" fill="none"/></svg></span><div><h4>Confidence Built In</h4><p>Trusted By Contractors And Developers<br>For Dependable Delivery</p></div></div>
<div class="reason" style="left:399px;top:3127px;width:240px"><span class="tick"><svg width="8" height="8" viewBox="0 0 8 8"><path d="M2.5 1l3 3-3 3" stroke="#fff" stroke-width="1.6" fill="none"/></svg></span><div><h4>Achieve Inclusion Goals</h4><p>Partnering With A Certified SBE, VBE,<br>SDVOSB, VFBE, And MBE-Ready Firm Helps<br>Meet Diversity Participation Requirements</p></div></div>
<div class="btn" style="left:156px;top:3215px;width:118px;height:31px">Contact Now</div>
<div class="dot" style="left:702px;top:2845px;width:62px;height:62px;background:var(--pink)"></div>
<div class="dot" style="left:988px;top:2858px;width:26px;height:26px;background:#c9cfdc"></div>
<div class="dot" style="left:770px;top:3175px;width:30px;height:30px;background:var(--pink)"></div>
<div class="why-photo" role="img" aria-label="Welder in a helmet welding with bright sparks"><div></div></div>

<!-- form -->
<section class="contact" role="img" aria-label="Dark blue workshop backdrop">
  <h2 class="heading" style="position:absolute;top:66px;left:0;width:1200px;text-align:center">Kindly Fill Below Form</h2>
  <p style="position:absolute;top:116px;left:0;width:1200px;text-align:center;font-size:11px;color:#fff">For Quotes, Bid Opportunities, Or Partnership Inquiries.</p>
</section>
<div class="field" style="left:244px;top:3480px"><label>Your Name</label><div class="input">type here</div></div>
<div class="field" style="left:487px;top:3480px"><label>Company Name</label><div class="input">type here</div></div>
<div class="field" style="left:731px;top:3480px"><label>Message</label><div class="input" style="height:96px">Type your massage</div></div>
<div class="field" style="left:244px;top:3548px"><label>Email Address</label><div class="input">you@example.com</div></div>
<div class="field" style="left:487px;top:3548px"><label>Phone Number</label><div class="input">(123) 456-7890</div></div>
<div class="btn" style="left:560px;top:3627px;width:80px;height:31px">Submit</div>

<!-- footer -->
<footer class="footer">
  <div class="dot" style="left:155px;top:43px;width:124px;height:124px;background:#fff;display:flex;align-items:center;justify-content:center;text-align:center;font-family:'Roboto',sans-serif;font-weight:900;font-size:14px;line-height:1.1;color:var(--navy)">Ridgeline<br>Forgecraft</div>
</footer>
<div class="foot-col" style="left:350px">
  <h5>CONTACT US</h5>
  <ul>
    <li><svg width="11" height="11" viewBox="0 0 24 24"><path fill="#c0123a" d="M6.6 10.8a15 15 0 0 0 6.6 6.6l2.2-2.2a1 1 0 0 1 1-.25 11.4 11.4 0 0 0 3.6.6 1 1 0 0 1 1 1V20a1 1 0 0 1-1 1A17 17 0 0 1 3 4a1 1 0 0 1 1-1h3.5a1 1 0 0 1 1 1c0 1.25.2 2.45.6 3.6a1 1 0 0 1-.25 1z"/></svg>555-014-2280</li>
    <li style="margin-top:12px"><svg width="11" height="11" viewBox="0 0 24 24"><path fill="#c0123a" d="M2 5h20v14H2zM2 5l10 8 10-8" stroke="#1c1d22" stroke-width="1.5"/></svg>info@ridgelineforgecraftllc.example</li>
    <li style="margin-top:12px"><svg width="11" height="13" viewBox="0 0 24 28"><path fill="#c0123a" d="M12 0a9 9 0 0 0-9 9c0 7 9 19 9 19s9-12 9-19a9 9 0 0 0-9-9zm0 12a3 3 0 1 1 0-6 3 3 0 0 1 0 6z"/></svg><span>48 Quarry Lane, Millbrook<br>Heights, 4521</span></li>
  </ul>
</div>
<div class="foot-col" style="left:612px">
  <h5>QUICK LINKS</h5>
  <ul><li style="color:var(--red)">Home</li><li>About Us</li><li>Products</li><li>Contact Us</li></ul>
</div>
<div class="footer-badges">
  <div class="dot" role="img" aria-label="Certification badge" style="left:27px;top:49px;width:110px;height:110px;border:6px solid #2a4aa0;background:#fff"></div>
  <div class="dot" role="img" aria-label="Certification badge" style="left:150px;top:49px;width:110px;height:110px;background:#111"></div>
</div>
<div class="bottom-bar">
  <span style="position:absolute;left:156px;top:9px">© 2025 Ridgeline Forgecraft. All Rights Reserved.</span>
  <span class="abs" style="left:965px;top:10px;width:11px;height:11px;background:#fff;border-radius:2px"></span>
  <span class="abs" style="left:993px;top:10px;width:11px;height:11px;border:1.5px solid #fff;border-radius:3px"></span>
  <span class="abs" style="left:1021px;top:5px;width:21px;height:21px;background:#fff;border-radius:50%"></span>
</div>

</body>
</html>
```